Brytmark Commercial Painting Services

create a one page 8.5x11 flyer with a blue and white picture if possible or compliment color scheme to blue and add this text as overlay. I have added one flyer as an example but i feel it needs to much better:
Brytmark
Commercial Painting Services
Transform Your Facility with Professional Painting

As a trusted provider of cleaning and maintenance services, Brytmark is proud to offer Commercial Painting solutions to keep your facility looking its best. Whether you need a fresh coat of paint to enhance your workspace or a complete overhaul to maintain a professional appearance, we’ve got you covered.

Why Choose Brytmark for Your Commercial Painting Needs?
✅ Expert Craftsmanship – Our skilled painters ensure smooth, high-quality finishes tailored to your facility’s needs.
✅ Minimal Disruption – We work around your schedule to minimize downtime and interruptions.
✅ Comprehensive Solutions – From surface preparation to the final coat, we handle it all.
✅ Safe & Eco-Friendly Products – We use high-quality, low-VOC paints for a healthier work environment.
✅ Seamless Integration – Combine painting with our cleaning services for a full maintenance package.

Industries We Serve:
✔ Office Buildings
✔ Warehouses & Industrial Spaces
✔ Retail Stores
✔ Healthcare Facilities
✔ Educational Institutions
✔ And More!

Enhance Your Space Today!
Let Brytmark bring new life to your facility with our professional painting services.

📞 905-555-0143
📧 support@brytmark.ca
📞 Toll-Free: 1-877-555-0178

```html
<!DOCTYPE html>
<html lang="en">
<head>
<meta charset="utf-8">
<title>Brytmark Commercial Painting Services</title>
<link href="https://fonts.googleapis.com/css2?family=Oswald:wght@400;500;600&family=Open+Sans:wght@400;600;700&family=Poppins:wght@400;700&display=swap" rel="stylesheet">
<style>
:root{
  --stage:#b4b4b4;
  --navy:#2b3a6c;
  --navy-deep:#222f5c;
  --brand-blue:#1b84c8;
  --bright-blue:#1f8fd6;
  --white:#ffffff;
  --ink:#111111;
  --supply-light:#f1f1f1;
  --supply-mid:#d9d9d9;
}
*{margin:0;padding:0;box-sizing:border-box}
html,body{width:779px;height:1200px;overflow:hidden}
body{background:var(--stage);position:relative;font-family:"Open Sans",sans-serif}
.flyer{position:absolute;left:0;top:96px;width:779px;height:1008px;background:var(--white);overflow:hidden}
.hero{position:absolute;left:0;top:0;width:779px;height:808px;
  background:linear-gradient(135deg,#2e3d72 0%,var(--navy) 45%,var(--navy-deep) 100%)}
.hero-photo{position:absolute;left:0;top:0;width:779px;height:808px;
  background:radial-gradient(ellipse at 72% 30%,rgba(80,100,160,.45),rgba(43,58,108,0) 60%)}
.brand-top{position:absolute;top:48px;left:0;width:779px;text-align:center;
  font-family:"Open Sans",sans-serif;font-weight:600;font-size:46px;letter-spacing:6px;color:var(--brand-blue)}
.title{position:absolute;left:0;width:779px;text-align:center;color:var(--white);font-family:"Oswald",sans-serif;line-height:1}
.title-1{top:130px;font-size:66px;font-weight:400;letter-spacing:-.5px}
.title-2{top:204px;font-size:66px;font-weight:600}
.tagline{position:absolute;top:277px;left:0;width:779px;text-align:center;
  color:var(--bright-blue);font-weight:600;font-size:19.5px;line-height:26px}
.intro{position:absolute;top:309px;left:86px;width:600px;color:var(--white);font-size:13.8px;line-height:16.4px}
.section-bar{position:absolute;height:26px;
  background:linear-gradient(90deg,var(--bright-blue) 0%,rgba(31,143,214,.55) 8%,rgba(31,143,214,0) 30%)}
.section-bar span{display:block;font-family:"Oswald",sans-serif;font-weight:500;color:var(--white);font-size:17.5px;line-height:26px;white-space:nowrap}
.why{top:392px;left:86px;width:600px}
.why span{padding-left:31px}
.feature{position:absolute;width:215px}
.feature h3{display:flex;align-items:center;gap:5px;color:var(--bright-blue);font-family:"Open Sans",sans-serif;font-weight:700;font-size:12.6px;white-space:nowrap}
.feature h3 svg{flex:none}
.feature p{color:var(--white);font-size:11.2px;line-height:15.4px;padding-left:17px;margin-top:3px}
.industries{position:absolute;top:611px;left:88px;width:603px;height:152px;border:2px dotted var(--bright-blue);border-radius:8px}
.industries-bar{top:598px;left:269px;width:190px;
  background:linear-gradient(90deg,var(--bright-blue) 0%,var(--bright-blue) 14%,rgba(31,143,214,0) 100%)}
.industries-bar span{text-align:center;padding-left:14px}
.industry{position:absolute;top:641px;width:130px;margin-left:-65px;text-align:center;color:#d9dff0;font-size:13.6px;line-height:17px}
.industry svg{display:block;margin:0 auto 13px}
.cta-band{position:absolute;top:808px;left:0;width:779px;height:75px;background:var(--brand-blue)}
.cta-title{position:absolute;top:818px;left:86px;font-family:"Oswald",sans-serif;font-weight:500;font-size:18px;color:var(--white)}
.cta-text{position:absolute;top:845px;left:86px;width:400px;font-size:11.2px;line-height:15.4px;color:var(--white)}
.supplies{position:absolute;left:500px;top:722px;width:279px;height:286px;border-radius:14px 0 0 0;
  background:linear-gradient(160deg,var(--supply-light) 0%,#e8e8e8 50%,var(--supply-mid) 100%)}
.phone{position:absolute;top:893px;left:96px;display:flex;align-items:center;gap:12px;
  font-family:"Poppins",sans-serif;font-weight:700;font-size:27px;color:var(--ink)}
.contact-lines{position:absolute;top:900px;left:332px;font-family:"Poppins",sans-serif;font-size:10.6px;line-height:13.5px;color:var(--ink)}
.brand-bottom{position:absolute;top:940px;left:88px;display:flex;align-items:center;gap:8px;
  font-family:"Open Sans",sans-serif;font-weight:600;font-size:28px;letter-spacing:3px;color:var(--brand-blue)}
.brand-bottom i{display:block;width:10px;height:10px;background:var(--brand-blue)}
</style>
</head>
<body>
<main class="flyer">
  <div class="hero"></div>
  <div class="hero-photo" role="img" aria-label="Painter on a lift rolling paint onto a tall building wall, toned in deep blue"></div>

  <div class="brand-top">BRYTMARK</div>
  <h1 class="title title-1">BRYTMARK COMMERCIAL</h1>
  <h1 class="title title-2">PAINTING SERVICES</h1>
  <p class="tagline">Transform Your Facility With Professional Painting</p>
  <p class="intro">As a trusted provider of cleaning and maintenance services, Brytmark is proud to offer Commercial Painting solutions to keep your facility looking its best. Whether you need a fresh coat of paint to enhance your workspace or a complete overhaul to maintain a professional appearance, we’ve got you covered.</p>

  <div class="section-bar why"><span>WHY CHOOSE BRYTMARK FOR YOUR COMMERCIAL PAINTING NEEDS?</span></div>

  <div class="feature" style="left:86px;top:434px">
    <h3><svg width="12" height="12" viewBox="0 0 12 12" fill="none" stroke="#1f8fd6" stroke-width="1.2"><rect x="1" y="1.5" width="9" height="9" rx="2"/><path d="M3.5 6l2 2 5-6"/></svg>Expert Craftsmanship</h3>
    <p>Our skilled painters ensure smooth, high-quality finishes tailored to your facility’s needs.</p>
  </div>
  <div class="feature" style="left:305px;top:434px;width:200px">
    <h3><svg width="12" height="12" viewBox="0 0 12 12" fill="none" stroke="#1f8fd6" stroke-width="1.2"><rect x="1" y="1.5" width="9" height="9" rx="2"/><path d="M3.5 6l2 2 5-6"/></svg>Minimal Disruption</h3>
    <p>We work around your schedule to minimize downtime and interruptions.</p>
  </div>
  <div class="feature" style="left:505px;top:434px;width:170px">
    <h3><svg width="12" height="12" viewBox="0 0 12 12" fill="none" stroke="#1f8fd6" stroke-width="1.2"><rect x="1" y="1.5" width="9" height="9" rx="2"/><path d="M3.5 6l2 2 5-6"/></svg>Seamless Integration</h3>
    <p>Combine painting with our cleaning services for a full maintenance package.</p>
  </div>
  <div class="feature" style="left:86px;top:522px">
    <h3><svg width="12" height="12" viewBox="0 0 12 12" fill="none" stroke="#1f8fd6" stroke-width="1.2"><rect x="1" y="1.5" width="9" height="9" rx="2"/><path d="M3.5 6l2 2 5-6"/></svg>Safe &amp; Eco-Friendly Products</h3>
    <p>We use high-quality, low-VOC paints for a healthier work environment</p>
  </div>
  <div class="feature" style="left:305px;top:522px;width:200px">
    <h3><svg width="12" height="12" viewBox="0 0 12 12" fill="none" stroke="#1f8fd6" stroke-width="1.2"><rect x="1" y="1.5" width="9" height="9" rx="2"/><path d="M3.5 6l2 2 5-6"/></svg>Comprehensive Solutions</h3>
    <p>From surface preparation to the final coat, we handle it all.</p>
  </div>

  <div class="industries"></div>
  <div class="section-bar industries-bar"><span>INDUSTRIES WE SERVE</span></div>

  <div class="industry" style="left:137px">
    <svg width="32" height="32" viewBox="0 0 32 32" fill="none" stroke="#1f8fd6" stroke-width="1.3"><rect x="6" y="10" width="14" height="20"/><rect x="20" y="18" width="7" height="12"/><path d="M10 14h2M14 14h2M10 19h2M14 19h2M11 30v-5h4v5M2 30h28"/><circle cx="24" cy="6" r="3"/><path d="M24 9v4"/></svg>
    Office<br>Buildings
  </div>
  <div class="industry" style="left:257px">
    <svg width="32" height="32" viewBox="0 0 32 32" fill="none" stroke="#1f8fd6" stroke-width="1.3"><path d="M3 30V11l13-7 13 7v19"/><rect x="8" y="14" width="16" height="16"/><path d="M8 18h16M8 22h16M8 26h16"/></svg>
    Warehouses &amp;<br>Industrial Spaces
  </div>
  <div class="industry" style="left:384px">
    <svg width="32" height="32" viewBox="0 0 32 32" fill="none" stroke="#1f8fd6" stroke-width="1.3"><rect x="10" y="3" width="12" height="10"/><path d="M16 5v6M13 8h6"/><rect x="3" y="13" width="26" height="17"/><path d="M7 17h3M7 22h3M22 17h3M22 22h3M13 30v-7h6v7"/></svg>
    Healthcare<br>Facilities
  </div>
  <div class="industry" style="left:491px">
    <svg width="32" height="32" viewBox="0 0 32 32" fill="none" stroke="#1f8fd6" stroke-width="1.3"><path d="M3 12l13-7 13 7H3z"/><path d="M6 12v14M11 12v14M21 12v14M26 12v14M2 27h28M16 2v3"/><circle cx="24" cy="24" r="5"/></svg>
    Educational<br>Institutions
  </div>
  <div class="industry" style="left:582px">
    <svg width="32" height="32" viewBox="0 0 32 32" fill="none" stroke="#1f8fd6" stroke-width="1.3"><rect x="11" y="2" width="10" height="6"/><path d="M4 8h24l2 5H2l2-5z"/><path d="M5 13v17h22V13M9 30v-9h6v9M18 18h6v5h-6z"/></svg>
    Retail<br>Stores
  </div>
  <div class="industry" style="left:654px">
    <svg width="32" height="32" viewBox="0 0 32 32" fill="none" stroke="#1f8fd6" stroke-width="1.3"><rect x="5" y="6" width="7" height="24"/><rect x="13" y="2" width="7" height="28"/><path d="M21 14h5v16M8 10v16M16 6v20"/><circle cx="27" cy="25" r="3"/></svg>
    And<br>More!
  </div>

  <div class="cta-band"></div>
  <h2 class="cta-title">ENHANCE YOUR SPACE TODAY!</h2>
  <p class="cta-text">Let Brytmark bring new life to your facility with our professional painting services.</p>

  <div class="supplies" role="img" aria-label="Paint bucket with brushes, roller, colour swatches and masking tape"></div>

  <div class="phone">
    <svg width="18" height="18" viewBox="0 0 24 24" fill="none" stroke="#1b84c8" stroke-width="2.2" stroke-linecap="round"><path d="M5 3h3l2 5-2.5 1.5a11 11 0 0 0 7 7L16 14l5 2v3a2 2 0 0 1-2 2A17 17 0 0 1 3 5a2 2 0 0 1 2-2z"/><path d="M15 3a6 6 0 0 1 6 6M15 7a2 2 0 0 1 2 2"/></svg>
    905-555-0143
  </div>
  <div class="contact-lines">support@brytmark.ca<br>Toll-Free: 1-877-555-0178</div>

  <div class="brand-bottom"><i></i>BRYTMARK</div>
</main>
</body>
</html>
```